Letterhead

Can you please design me a letterhead that I can use electronically in word as a template. I have attached my business card as I would like the design to reflect this logo.

```html
<!DOCTYPE html>
<html lang="en">
<head>
<meta charset="utf-8">
<title>Meridale Letterhead</title>
<link rel="stylesheet" href="https://fonts.googleapis.com/css2?family=Open+Sans:wght@400;600;700&family=Arimo:wght@700&display=swap">
<style>
  :root {
    --backdrop: #ffffff;
    --paper: #ffffff;
    --brand-red: #b31f24;
    --ink: #1a1a1a;
    --ink-soft: #333333;
    --band-black: #000000;
  }
  * { margin: 0; padding: 0; box-sizing: border-box; }
  html, body {
    width: 1200px;
    height: 900px;
    overflow: hidden;
    background: var(--backdrop);
  }
  .canvas {
    position: relative;
    width: 1200px;
    height: 900px;
  }
  .letterhead {
    position: absolute;
    left: 344px;
    top: 89px;
    width: 511px;
    height: 723px;
    background: var(--paper);
    box-shadow: 0 0 10px rgba(0, 0, 0, 0.35);
  }
  .brand {
    position: absolute;
    left: 23px;
    top: 16px;
  }
  .brand-name {
    font-family: "Open Sans", Arial, sans-serif;
    font-weight: 600;
    font-size: 42px;
    line-height: 1;
    letter-spacing: -0.5px;
    color: var(--brand-red);
  }
  .brand-descriptor {
    margin-top: 1px;
    margin-left: 3px;
    font-family: "Arimo", Arial, sans-serif;
    font-weight: 700;
    font-size: 8.5px;
    color: var(--band-black);
  }
  .contact {
    position: absolute;
    right: 24px;
    top: 31px;
    text-align: right;
    font-family: "Open Sans", Arial, sans-serif;
    font-size: 6.8px;
    line-height: 1.25;
    color: var(--ink-soft);
  }
  .contact-name {
    font-weight: 700;
    font-size: 8px;
    color: var(--ink);
  }
  .contact-role {
    color: var(--brand-red);
    margin-bottom: 6px;
  }
  .contact-label {
    color: var(--brand-red);
  }
  .edge-band {
    position: absolute;
    right: 0;
    top: 0;
    width: 12px;
    height: 100%;
  }
  .edge-band-red {
    height: 623px;
    background: var(--brand-red);
  }
  .edge-band-black {
    height: 100px;
    background: var(--band-black);
  }
</style>
</head>
<body>
  <main class="canvas">
    <section class="letterhead">
      <header class="brand">
        <div class="brand-name">meridale</div>
        <div class="brand-descriptor">Business Consultants Pty Ltd</div>
      </header>

      <address class="contact" style="font-style: normal;">
        <div class="contact-name">Helena Marsh</div>
        <div class="contact-role">Principal</div>
        <div><span class="contact-label">P</span> : 0400 555 182</div>
        <div><span class="contact-label">E</span> : helena@meridale.net.au</div>
        <div><span class="contact-label">ACN</span> : 081 442 306</div>
      </address>

      <div class="edge-band">
        <div class="edge-band-red"></div>
        <div class="edge-band-black"></div>
      </div>
    </section>
  </main>
</body>
</html>
```